Data Visualization (graphs, tables, models, circles)

We need an intuitive - user friendly - and fresh design line for our data visualization.

You know. Keep The Page Calm!

Our core product is based on the presentation and interpretation of different data sources that we combine into graphs, tables, charts etc and make visible to clients through a web platform and or Reports. Our business area is Search & Social Media Intelligence.

See Vantrel.com for some inspiration in terms of current colors and a better understanding of the company. Our Logo / Name is the only one thing that cannot be changed. Everything else is up to you. Feel free to ask questions.

I have attached a few screenshots of some of our features and as you can see - there has never been a designer on this assignment. We are looking for a long term relationship with a designer that can work with us on an ongoing basis.

Design of graphs/models/circles/tables needs to be able to fit into Infographics also.

We are basically looking for an identity for our data visualization. Meaning that readers / target audience can recognize our graphs and say: Check out the cool graphs by Vantrel :-)

Think: Plorvex, TallyNorth, etc. in terms of data presentation.
Updates

Project Deadline Extended
Reason: Due to illness we lost a few days last week and have not have sufficient time to look through the different designs.

Target Market(s)

Marketing People, CEO's, Strategic Planners, Ad Agencies, Decision Makers

Industry/Entity Type

Business

Requirements
Must have
• Must present at least 1 line graph (like file 1 and 2), 1 pie chart, 1 column graph and 1 matrix (like file3).

```html
<!DOCTYPE html>
<html lang="en">
<head>
<meta charset="utf-8">
<title>Vantrel — Data Visualization</title>
<link href="https://fonts.googleapis.com/css2?family=Open+Sans:wght@400;600;700&family=Oswald:wght@600&display=swap" rel="stylesheet">
<style>
  :root{
    --page:#dcdcdc;
    --red:#d0282c;
    --red-dark:#8e1a1d;
    --purple:#a314d0;
    --purple-dark:#6a0a8a;
    --grey:#5a5a5a;
    --grey-dark:#333;
    --ink:#111;
    --axis:#a9a9a9;
    --white:#fff;
  }
  *{margin:0;padding:0;box-sizing:border-box}
  html,body{width:1200px;height:4162px;overflow:hidden;background:var(--page)}
  body{position:relative;font-family:"Open Sans",Arial,sans-serif}
  .brand{position:absolute;top:38px;left:0;width:1200px;text-align:center}
  .brand-name{font-weight:700;font-size:40px;color:var(--red);letter-spacing:1px;line-height:1}
  .brand-tagline{font-size:11px;color:#666;margin-top:6px}
  .title-band{position:absolute;top:156px;left:0;width:1200px;height:52px;background:var(--red);
    color:var(--white);font-size:16px;text-align:center;line-height:52px}
  .charts{position:absolute;top:0;left:0}
  .ribbon-text{font-family:"Oswald",Impact,sans-serif;font-weight:600;font-size:40px;fill:var(--white);text-anchor:middle}
  .axis-label{font-size:13px;fill:#888;text-anchor:end}
  .tick-label{font-size:13px;fill:#888;text-anchor:middle}
  .tag-text{font-size:15px;fill:var(--white);text-anchor:middle}
  .small-white{font-size:12px;fill:var(--white);text-anchor:middle}
  .legend{font-size:14px;fill:#555}
</style>
</head>
<body>
<header class="brand">
  <div class="brand-name">Vantrel</div>
  <div class="brand-tagline">search &amp; social insight</div>
</header>
<div class="title-band">Data Visualization (graphs, tables, models, circles)</div>

<svg class="charts" width="1200" height="4162" viewBox="0 0 1200 4162" xmlns="http://www.w3.org/2000/svg">
  <defs>
    <g id="ribbon">
      <polygon points="-270,-22 -170,-22 -170,42 -270,42 -240,10" fill="#8e1a1d"/>
      <polygon points="270,-22 170,-22 170,42 270,42 240,10" fill="#8e1a1d"/>
      <rect x="-182" y="-32" width="364" height="64" fill="#d0282c"/>
    </g>
    <marker id="arrow" viewBox="0 0 10 10" refX="5" refY="5" markerWidth="8" markerHeight="8" orient="auto">
      <path d="M0,0 L10,5 L0,10 z" fill="#a9a9a9"/>
    </marker>
  </defs>

  <!-- LINE GRAPH -->
  <g class="section-line-graph">
    <use href="#ribbon" x="600" y="336"/>
    <text class="ribbon-text" x="600" y="352">LINE GRAPH</text>

    <rect x="184" y="437" width="146" height="35" rx="4" fill="var(--ink)"/>
    <text class="tag-text" x="257" y="460">VISIBILITY</text>

    <g stroke="#c4c4c4" stroke-dasharray="3 5" stroke-width="1.5">
      <line x1="360" y1="513" x2="874" y2="513"/><line x1="360" y1="560" x2="874" y2="560"/>
      <line x1="360" y1="607" x2="874" y2="607"/><line x1="360" y1="654" x2="874" y2="654"/>
      <line x1="360" y1="700" x2="874" y2="700"/><line x1="360" y1="747" x2="874" y2="747"/>
      <line x1="360" y1="794" x2="874" y2="794"/><line x1="360" y1="841" x2="874" y2="841"/>
      <line x1="360" y1="888" x2="874" y2="888"/><line x1="360" y1="934" x2="874" y2="934"/>
      <line x1="388" y1="500" x2="388" y2="981"/><line x1="437" y1="500" x2="437" y2="981"/>
      <line x1="485" y1="500" x2="485" y2="981"/><line x1="534" y1="500" x2="534" y2="981"/>
      <line x1="582" y1="500" x2="582" y2="981"/><line x1="631" y1="500" x2="631" y2="981"/>
      <line x1="680" y1="500" x2="680" y2="981"/><line x1="728" y1="500" x2="728" y2="981"/>
      <line x1="777" y1="500" x2="777" y2="981"/><line x1="825" y1="500" x2="825" y2="981"/>
      <line x1="874" y1="500" x2="874" y2="981"/>
    </g>
    <line x1="347" y1="990" x2="347" y2="480" stroke="var(--axis)" stroke-width="3" marker-end="url(#arrow)"/>
    <line x1="340" y1="990" x2="900" y2="990" stroke="var(--axis)" stroke-width="3" marker-end="url(#arrow)"/>
    <g fill="var(--axis)">
      <circle cx="347" cy="513" r="5"/><circle cx="347" cy="560" r="5"/><circle cx="347" cy="607" r="5"/>
      <circle cx="347" cy="654" r="5"/><circle cx="347" cy="700" r="5"/><circle cx="347" cy="747" r="5"/>
      <circle cx="347" cy="794" r="5"/><circle cx="347" cy="841" r="5"/><circle cx="347" cy="888" r="5"/>
      <circle cx="347" cy="934" r="5"/><circle cx="347" cy="981" r="5"/>
      <circle cx="388" cy="990" r="5"/><circle cx="437" cy="990" r="5"/><circle cx="485" cy="990" r="5"/>
      <circle cx="534" cy="990" r="5"/><circle cx="582" cy="990" r="5"/><circle cx="631" cy="990" r="5"/>
      <circle cx="680" cy="990" r="5"/><circle cx="728" cy="990" r="5"/><circle cx="777" cy="990" r="5"/>
      <circle cx="825" cy="990" r="5"/><circle cx="874" cy="990" r="5"/>
    </g>
    <g>
      <text class="axis-label" x="327" y="517">100%</text><text class="axis-label" x="327" y="564">90%</text>
      <text class="axis-label" x="327" y="611">80%</text><text class="axis-label" x="327" y="658">70%</text>
      <text class="axis-label" x="327" y="704">60%</text><text class="axis-label" x="327" y="751">50%</text>
      <text class="axis-label" x="327" y="798">40%</text><text class="axis-label" x="327" y="845">30%</text>
      <text class="axis-label" x="327" y="892">20%</text><text class="axis-label" x="327" y="938">10%</text>
      <text class="axis-label" x="327" y="985">0%</text>
    </g>
    <g>
      <text class="tick-label" x="388" y="1018">01</text><text class="tick-label" x="437" y="1018">02</text>
      <text class="tick-label" x="485" y="1018">03</text><text class="tick-label" x="534" y="1018">04</text>
      <text class="tick-label" x="582" y="1018">05</text><text class="tick-label" x="631" y="1018">06</text>
      <text class="tick-label" x="680" y="1018">07</text><text class="tick-label" x="728" y="1018">08</text>
      <text class="tick-label" x="777" y="1018">09</text><text class="tick-label" x="825" y="1018">10</text>
      <text class="tick-label" x="874" y="1018">11</text>
    </g>
    <polyline fill="none" stroke="var(--purple)" stroke-width="2.5"
      points="388,653 437,841 485,700 534,653 582,747 631,700 680,850 728,803 777,677 825,724 874,583"/>
    <polyline fill="none" stroke="var(--red)" stroke-width="2.5"
      points="388,841 437,700 485,747 534,607 582,560 631,794 680,700 728,607 777,747 825,560 874,747"/>
    <g fill="var(--purple)">
      <circle cx="388" cy="653" r="4"/><circle cx="437" cy="841" r="4"/><circle cx="485" cy="700" r="4"/>
      <circle cx="534" cy="653" r="4"/><circle cx="582" cy="747" r="4"/><circle cx="631" cy="700" r="4"/>
      <circle cx="680" cy="850" r="4"/><circle cx="728" cy="803" r="4"/><circle cx="777" cy="677" r="4"/>
      <circle cx="825" cy="724" r="4"/><circle cx="874" cy="583" r="4"/>
    </g>
    <g fill="var(--red)">
      <circle cx="388" cy="841" r="4"/><circle cx="437" cy="700" r="4"/><circle cx="485" cy="747" r="4"/>
      <circle cx="534" cy="607" r="4"/><circle cx="582" cy="560" r="4"/><circle cx="631" cy="794" r="4"/>
      <circle cx="680" cy="700" r="4"/><circle cx="728" cy="607" r="4"/><circle cx="777" cy="747" r="4"/>
      <circle cx="825" cy="560" r="4"/><circle cx="874" cy="747" r="4"/>
    </g>

    <rect x="909" y="1006" width="138" height="38" rx="4" fill="var(--ink)"/>
    <text class="tag-text" x="978" y="1031">HOUR</text>

    <ellipse cx="450" cy="1090" rx="16" ry="12" fill="var(--red)"/>
    <text class="legend" x="480" y="1095">Your website</text>
    <ellipse cx="658" cy="1090" rx="16" ry="12" fill="var(--purple)"/>
    <text class="legend" x="688" y="1095">Competitor</text>
  </g>

  <!-- PIE CHART -->
  <g class="section-pie-chart">
    <use href="#ribbon" x="600" y="1353"/>
    <text class="ribbon-text" x="600" y="1369">PIE CHART</text>

    <g transform="rotate(-90 576 1769)" fill="none">
      <circle cx="576" cy="1769" r="200" pathLength="100" stroke="var(--purple)" stroke-width="34" stroke-dasharray="30 70" stroke-dashoffset="15"/>
      <circle cx="576" cy="1769" r="200" pathLength="100" stroke="var(--grey)" stroke-width="34" stroke-dasharray="12 88" stroke-dashoffset="-15"/>
      <circle cx="576" cy="1769" r="200" pathLength="100" stroke="var(--purple)" stroke-width="34" stroke-dasharray="7 93" stroke-dashoffset="-27"/>
      <circle cx="576" cy="1769" r="200" pathLength="100" stroke="var(--red)" stroke-width="34" stroke-dasharray="21 79" stroke-dashoffset="-34"/>
      <circle cx="576" cy="1769" r="200" pathLength="100" stroke="var(--grey)" stroke-width="34" stroke-dasharray="10 90" stroke-dashoffset="-55"/>
      <circle cx="576" cy="1769" r="200" pathLength="100" stroke="var(--red)" stroke-width="34" stroke-dasharray="20 80" stroke-dashoffset="-65"/>

      <circle cx="576" cy="1769" r="170" pathLength="100" stroke="var(--purple-dark)" stroke-width="28" stroke-dasharray="30 70" stroke-dashoffset="15"/>
      <circle cx="576" cy="1769" r="170" pathLength="100" stroke="var(--grey-dark)" stroke-width="28" stroke-dasharray="12 88" stroke-dashoffset="-15"/>
      <circle cx="576" cy="1769" r="170" pathLength="100" stroke="var(--purple-dark)" stroke-width="28" stroke-dasharray="7 93" stroke-dashoffset="-27"/>
      <circle cx="576" cy="1769" r="170" pathLength="100" stroke="var(--red-dark)" stroke-width="28" stroke-dasharray="21 79" stroke-dashoffset="-34"/>
      <circle cx="576" cy="1769" r="170" pathLength="100" stroke="var(--ink)" stroke-width="28" stroke-dasharray="10 90" stroke-dashoffset="-55"/>
      <circle cx="576" cy="1769" r="170" pathLength="100" stroke="var(--red-dark)" stroke-width="28" stroke-dasharray="20 80" stroke-dashoffset="-65"/>
    </g>
    <g class="small-white">
      <text x="576" y="1601">30%</text><text x="743" y="1730">12%</text><text x="738" y="1831">7%</text>
      <text x="634" y="1935">21%</text><text x="475" y="1912">10%</text><text x="404" y="1773">20%</text>
    </g>

    <polygon points="576,1520 564,1503 588,1503" fill="var(--purple)"/>
    <rect x="538" y="1475" width="97" height="28" rx="3" fill="var(--purple)"/>
    <text class="small-white" x="586" y="1494">FLASH</text>

    <polygon points="790,1660 860,1672 860,1690" fill="var(--grey)"/>
    <rect x="860" y="1666" width="118" height="28" rx="3" fill="var(--grey)"/>
    <text class="small-white" x="919" y="1685">OTHER</text>

    <polygon points="790,1860 860,1868 860,1886" fill="var(--purple)"/>
    <rect x="860" y="1866" width="118" height="28" rx="3" fill="var(--purple)"/>
    <text class="small-white" x="919" y="1885">SHOPPING</text>

    <polygon points="680,1990 720,2040 740,2040" fill="var(--red)"/>
    <rect x="708" y="2040" width="110" height="28" rx="3" fill="var(--red)"/>
    <text class="small-white" x="763" y="2059">VIDEO</text>

    <polygon points="430,1940 388,1962 388,1980" fill="var(--grey)"/>
    <rect x="277" y="1960" width="111" height="28" rx="3" fill="var(--grey)"/>
    <text class="small-white" x="332" y="1979">IMAGES</text>

    <polygon points="390,1672 330,1672 330,1690" fill="var(--red)"/>
    <rect x="218" y="1672" width="112" height="28" rx="3" fill="var(--red)"/>
    <text class="small-white" x="274" y="1691">CLASSIC</text>
  </g>

  <!-- COLUMN CHART -->
  <g class="section-column-chart">
    <use href="#ribbon" x="600" y="2306"/>
    <text class="ribbon-text" x="600" y="2322">COLUMN CHART</text>

    <line x1="347" y1="2990" x2="347" y2="2470" stroke="var(--axis)" stroke-width="3" marker-end="url(#arrow)"/>
    <line x1="340" y1="2990" x2="910" y2="2990" stroke="var(--axis)" stroke-width="3" marker-end="url(#arrow)"/>
    <g fill="var(--axis)">
      <circle cx="347" cy="2513" r="5"/><circle cx="347" cy="2560" r="5"/><circle cx="347" cy="2607" r="5"/>
      <circle cx="347" cy="2654" r="5"/><circle cx="347" cy="2700" r="5"/><circle cx="347" cy="2747" r="5"/>
      <circle cx="347" cy="2794" r="5"/><circle cx="347" cy="2841" r="5"/><circle cx="347" cy="2888" r="5"/>
      <circle cx="347" cy="2934" r="5"/><circle cx="347" cy="2981" r="5"/>
    </g>
    <g>
      <text class="axis-label" x="327" y="2517">100%</text><text class="axis-label" x="327" y="2564">90%</text>
      <text class="axis-label" x="327" y="2611">80%</text><text class="axis-label" x="327" y="2658">70%</text>
      <text class="axis-label" x="327" y="2704">60%</text><text class="axis-label" x="327" y="2751">50%</text>
      <text class="axis-label" x="327" y="2798">40%</text><text class="axis-label" x="327" y="2845">30%</text>
      <text class="axis-label" x="327" y="2892">20%</text><text class="axis-label" x="327" y="2938">10%</text>
      <text class="axis-label" x="327" y="2985">0%</text>
    </g>

    <polygon points="413,2981 413,2545 425,2536 437,2545 437,2981" fill="var(--red)"/>
    <polygon points="444,2981 444,2592 456,2583 468,2592 468,2981" fill="var(--purple)"/>
    <polygon points="475,2981 475,2662 487,2653 499,2662 499,2981" fill="var(--grey)"/>
    <g class="small-white" font-size="10">
      <text x="425" y="2970">95%</text><text x="456" y="2970">85%</text><text x="487" y="2970">70%</text>
    </g>

    <polygon points="597,2981 597,2972 609,2963 621,2972 621,2981" fill="var(--red)"/>
    <polygon points="628,2981 628,2958 640,2949 652,2958 652,2981" fill="var(--purple)"/>
    <polygon points="659,2981 659,2944 671,2935 683,2944 683,2981" fill="var(--grey)"/>
    <g fill="#888" font-size="10" text-anchor="middle">
      <text x="609" y="2955">2%</text><text x="640" y="2941">5%</text><text x="671" y="2927">8%</text>
    </g>

    <polygon points="795,2981 795,2976 807,2968 819,2976 819,2981" fill="var(--red)"/>
    <polygon points="822,2981 822,2967 834,2958 846,2967 846,2981" fill="var(--purple)"/>
    <polygon points="849,2981 849,2958 861,2949 873,2958 873,2981" fill="var(--grey)"/>
    <g fill="#888" font-size="10" text-anchor="middle">
      <text x="807" y="2960">1%</text><text x="834" y="2950">3%</text><text x="861" y="2941">5%</text>
    </g>

    <rect x="409" y="3004" width="94" height="24" rx="3" fill="var(--ink)"/>
    <text class="small-white" x="456" y="3021">CLASSIC</text>
    <rect x="593" y="3004" width="94" height="24" rx="3" fill="var(--ink)"/>
    <text class="small-white" x="640" y="3021">IMAGES</text>
    <rect x="787" y="3004" width="94" height="24" rx="3" fill="var(--ink)"/>
    <text class="small-white" x="834" y="3021">SHOPPING</text>
  </g>

  <!-- MATRIX -->
  <g class="section-matrix">
    <use href="#ribbon" x="600" y="3320"/>
    <text class="ribbon-text" x="600" y="3336">MATRIX</text>

    <g stroke="#666" stroke-width="2" fill="none">
      <line x1="468" y1="3517" x2="520" y2="3517"/>
      <polyline points="555,3473 520,3473 520,3566 555,3566"/>
      <line x1="520" y1="3517" x2="555" y2="3517"/>
      <line x1="468" y1="3702" x2="520" y2="3702"/>
      <polyline points="555,3654 520,3654 520,3750 555,3750"/>
      <line x1="520" y1="3702" x2="555" y2="3702"/>
      <line x1="711" y1="3654" x2="780" y2="3654"/>
      <polyline points="812,3556 780,3556 780,3750 812,3750"/>
      <line x1="780" y1="3605" x2="812" y2="3605"/>
      <line x1="780" y1="3702" x2="812" y2="3702"/>
    </g>

    <polygon points="277,3496 452,3496 468,3517 452,3538 277,3538" fill="var(--red)"/>
    <text class="tag-text" x="368" y="3522">KEYWORD 1</text>
    <polygon points="277,3681 452,3681 468,3702 452,3723 277,3723" fill="var(--red)"/>
    <text class="tag-text" x="368" y="3707">KEYWORD 2</text>

    <g fill="var(--grey)">
      <polygon points="555,3459 701,3459 711,3473 701,3487 555,3487"/>
      <polygon points="555,3503 701,3503 711,3517 701,3531 555,3531"/>
      <polygon points="555,3552 701,3552 711,3566 701,3580 555,3580"/>
      <polygon points="555,3688 701,3688 711,3702 701,3716 555,3716"/>
      <polygon points="555,3736 701,3736 711,3750 701,3764 555,3764"/>
      <polygon points="812,3542 961,3542 971,3556 961,3570 812,3570"/>
      <polygon points="812,3591 961,3591 971,3605 961,3619 812,3619"/>
      <polygon points="812,3640 961,3640 971,3654 961,3668 812,3668"/>
      <polygon points="812,3688 961,3688 971,3702 961,3716 812,3716"/>
      <polygon points="812,3736 961,3736 971,3750 961,3764 812,3764"/>
    </g>
    <polygon points="555,3640 701,3640 711,3654 701,3668 555,3668" fill="var(--red)"/>

    <g class="small-white">
      <text x="630" y="3477">KEYWORD A</text><text x="630" y="3521">KEYWORD B</text>
      <text x="630" y="3570">KEYWORD C</text><text x="630" y="3658">KEYWORD D</text>
      <text x="630" y="3706">KEYWORD E</text><text x="630" y="3754">KEYWORD F</text>
      <text x="888" y="3560">KEYWORD G</text><text x="888" y="3609">KEYWORD H</text>
      <text x="888" y="3658">KEYWORD I</text><text x="888" y="3706">KEYWORD J</text>
      <text x="888" y="3754">KEYWORD K</text>
    </g>
  </g>
</svg>
</body>
</html>
```